Website redesign and new logo

Hi we feel that the colours, layout and style along with the logo which is only text at the moment is poor. It seems to lack a quality and luxurious feel and we are about selling high end curtains. The text logo is hard to read as well in my opinion. We are looking for a overall revamp and an new logo. We want to maintain the main parts of the home page but happy to consider any ideas that will improve web traffic. It does not really reflect our achievements either of having curtains recently featured on Horizon 7 tv.
The website in question is www.lunaviewinteriors.co.uk

```html
<!DOCTYPE html>
<html lang="en">
<head>
<meta charset="utf-8">
<title>Luna View Interiors – Areas We Cover</title>
<link href="https://fonts.googleapis.com/css2?family=Inter:wght@300;400&display=swap" rel="stylesheet">
<style>
  :root {
    --page-white: #ffffff;
    --section-grey: #efefef;
    --text-dark: #2b2b2b;
    --text-body: #3a3a3a;
    --label-grey: #4a4a4a;
    --player-bar: #2a2a2a;
    --player-ctrl: #9a9a9a;
    --teal-band: #4a9995;
    --teal-glow: #49c6c2;
    --area-1: #5aa9a6;
    --area-2: #4a9793;
    --area-3: #33706d;
    --area-4: #5bc0bc;
    --area-5: #4a9a96;
    --area-6: #79b3b0;
    --photo-a: #c9b79a;
    --photo-b: #b59a73;
    --photo-c: #d7d4cc;
    --photo-d: #a48a74;
  }
  * { margin: 0; padding: 0; box-sizing: border-box; }
  html, body { width: 1200px; height: 800px; overflow: hidden; }
  body {
    position: relative;
    font-family: "Inter", "Helvetica Neue", Arial, sans-serif;
    background: var(--section-grey);
    color: var(--text-dark);
  }

  /* Intro section */
  .intro {
    position: absolute; left: 0; top: 0; width: 1200px; height: 147px;
    background: var(--page-white);
    box-shadow: 0 6px 14px rgba(0,0,0,0.12);
    z-index: 2;
  }
  .intro-copy {
    position: absolute; left: 150px; top: -9px; width: 440px;
    font-size: 13.5px; line-height: 17px; color: var(--text-body);
  }
  .video-player {
    position: absolute; left: 656px; top: 0; width: 372px; height: 73px;
    background: linear-gradient(90deg, #d8c9a8, #efe6d2 40%, #cdb892 70%, #e8dcc4);
  }
  .video-frame { position: absolute; inset: 0 0 35px 0; }
  .video-controls {
    position: absolute; left: 0; bottom: 0; width: 100%; height: 35px;
    background: var(--player-bar);
    display: flex; align-items: center; padding: 0 10px; gap: 14px;
    font-size: 11px; color: var(--player-ctrl);
  }
  .video-controls .time { color: #d0d0d0; }
  .video-controls .spacer { flex: 1; }
  .video-controls .host-name { font-size: 11px; color: var(--player-ctrl); }

  /* Areas section */
  .areas { position: absolute; left: 0; top: 147px; width: 1200px; height: 417px; }
  .areas-title {
    position: absolute; top: 94px; width: 100%; text-align: center;
    font-weight: 300; font-size: 22px; line-height: 30px; color: var(--text-dark);
  }
  .area {
    position: absolute; top: 155px; width: 150px; margin-left: -75px; text-align: center;
  }
  .area-badge {
    display: block; width: 104px; height: 104px; margin: 0 auto;
    border-radius: 50%; border: 2px solid rgba(255,255,255,0.35);
  }
  .area-name {
    margin-top: 11px; font-size: 13.5px; line-height: 16px; color: var(--label-grey);
  }

  /* Gallery band */
  .gallery {
    position: absolute; left: 0; top: 564px; width: 1200px; height: 236px;
    background: linear-gradient(180deg, var(--teal-glow) 0, var(--teal-band) 10px, var(--teal-band) 100%);
  }
  .gallery-title {
    position: absolute; top: 60px; width: 100%; text-align: center;
    font-weight: 300; font-size: 22px; line-height: 30px; color: #ffffff;
  }
  .gallery-photo { position: absolute; top: 130px; height: 106px; width: 254px; }
</style>
</head>
<body>

<section class="intro">
  <p class="intro-copy">so you can study and see how they are manufactured. We have a extensive range of fabric from which our handmade curtains or made measure curtains can be produced from.</p>
  <div class="video-player">
    <div class="video-frame" role="img" aria-label="Video still of a curtained room"></div>
    <div class="video-controls">
      <svg width="12" height="12" viewBox="0 0 12 12"><path d="M2 1 L11 6 L2 11 Z" fill="#9a9a9a"/></svg>
      <svg width="16" height="12" viewBox="0 0 16 12"><path d="M1 4 H4 L8 1 V11 L4 8 H1 Z" fill="#9a9a9a"/><path d="M10 3 Q13 6 10 9" stroke="#9a9a9a" fill="none" stroke-width="1.4"/></svg>
      <span class="time">0:00 / 5:57</span>
      <span class="spacer"></span>
      <svg width="12" height="12" viewBox="0 0 12 12"><circle cx="6" cy="6" r="5" fill="none" stroke="#9a9a9a" stroke-width="1.5"/><path d="M6 3 V6 H8" stroke="#9a9a9a" fill="none" stroke-width="1.3"/></svg>
      <span class="host-name">Streamly</span>
      <svg width="14" height="14" viewBox="0 0 14 14"><path d="M1 5 V1 H5 M9 1 H13 V5 M13 9 V13 H9 M5 13 H1 V9" stroke="#9a9a9a" fill="none" stroke-width="1.6"/></svg>
    </div>
  </div>
</section>

<section class="areas">
  <h2 class="areas-title">The areas we cover include</h2>
  <div class="area" style="left:254px"><span class="area-badge" style="background:var(--area-1)" role="img" aria-label="Curtain icon"></span><p class="area-name">Curtains<br>Berkshire</p></div>
  <div class="area" style="left:385px"><span class="area-badge" style="background:var(--area-2)" role="img" aria-label="Curtain icon"></span><p class="area-name">Curtains<br>Buckinghamshire</p></div>
  <div class="area" style="left:517px"><span class="area-badge" style="background:var(--area-3)" role="img" aria-label="Curtain icon"></span><p class="area-name">Curtains<br>Oxfordshire</p></div>
  <div class="area" style="left:651px"><span class="area-badge" style="background:var(--area-4)" role="img" aria-label="Curtain icon"></span><p class="area-name">Curtains<br>Winchester</p></div>
  <div class="area" style="left:780px"><span class="area-badge" style="background:var(--area-5)" role="img" aria-label="Curtain icon"></span><p class="area-name">Curtains<br>Guildford</p></div>
  <div class="area" style="left:910px"><span class="area-badge" style="background:var(--area-6)" role="img" aria-label="Curtain icon"></span><p class="area-name">Curtains<br>Oxford</p></div>
</section>

<section class="gallery">
  <h2 class="gallery-title">Our Curtains Gallery</h2>
  <div class="gallery-photo" style="left:59px; background:linear-gradient(135deg,var(--photo-a),#e6dccb)" role="img" aria-label="Photo of curtains in a bright living room"></div>
  <div class="gallery-photo" style="left:336px; background:linear-gradient(135deg,var(--photo-b),#d9c6a4)" role="img" aria-label="Photo of draped curtains with pelmet"></div>
  <div class="gallery-photo" style="left:613px; background:linear-gradient(135deg,var(--photo-c),#f1efea)" role="img" aria-label="Photo of pale curtains at a window"></div>
  <div class="gallery-photo" style="left:890px; background:linear-gradient(135deg,var(--photo-d),#cdb9a4)" role="img" aria-label="Photo of curtains in a bedroom"></div>
</section>

</body>
</html>
```